Recruitment Poster KSE and KPE

Need a poster for new singers : for the Marsa Student Singers and for our new initiative Marsa Primary Singers. The target audience for the Student Singers is young teens (13-18) and for the Primary Singers is parents of kids aged 7-10. Both choirs need to appeal more to boys as girls are more easily recruited into choir.

```html
<!DOCTYPE html>
<html lang="en">
<head>
<meta charset="utf-8">
<title>Calling Young Singers – Marsa Student Singers</title>
<link href="https://fonts.googleapis.com/css2?family=Oswald:wght@400;500;600&family=Open+Sans:wght@600;700&display=swap" rel="stylesheet">
<style>
  :root {
    --backdrop: #e6e6e4;
    --paper: #ffffff;
    --ink: #111111;
    --red: #e2262b;
    --red-dark: #a8181c;
    --footer: #0d0d0d;
    --footer-text: #ffffff;
    --link-blue: #9fb4e0;
  }
  * { box-sizing: border-box; margin: 0; padding: 0; }
  html, body {
    width: 1200px; height: 1148px; overflow: hidden;
    background: var(--backdrop);
  }
  .poster {
    position: absolute; left: 210px; top: 24px;
    width: 780px; height: 1100px;
    background: var(--paper);
    font-family: "Oswald", sans-serif;
    color: var(--ink);
    overflow: hidden;
  }
  .portrait {
    position: absolute; left: 98px; top: 20px;
    width: 386px; height: 436px;
    background: linear-gradient(180deg, #1a1a1a 0%, #000 100%);
    border-radius: 140px 140px 0 0;
  }
  .brand {
    position: absolute; right: 80px; top: 75px;
    text-align: center; color: var(--ink);
  }
  .brand-name {
    font-family: "Oswald", sans-serif; font-weight: 500;
    font-size: 34px; letter-spacing: 1px; line-height: 1;
    display: flex; align-items: center; gap: 8px; justify-content: center;
  }
  .brand-dot { width: 14px; height: 14px; border-radius: 50%; background: var(--red); }
  .brand-sub {
    font-family: "Oswald", sans-serif; font-weight: 500;
    font-size: 10px; letter-spacing: .5px; margin-top: 4px; text-transform: uppercase;
  }
  .headline-band {
    position: absolute; left: 60px; top: 456px;
    width: 680px; height: 136px;
    background: var(--red);
    display: flex; align-items: center; justify-content: center;
  }
  .headline {
    font-weight: 500; font-size: 78px; letter-spacing: -1px;
    color: var(--ink); text-transform: uppercase; line-height: 1;
    transform: scaleX(.82);
    white-space: nowrap;
  }
  .invite {
    position: absolute; left: 0; right: 0; top: 620px;
    text-align: center; color: var(--red);
    font-weight: 500; font-size: 33px; line-height: 1.2;
    text-transform: uppercase; transform: scaleX(.86);
  }
  .needs-you {
    position: absolute; left: 0; right: 0; top: 733px;
    text-align: center; font-weight: 500; font-size: 52px;
    text-transform: uppercase; line-height: 1; white-space: nowrap;
    transform: scaleX(.78);
  }
  .start-ribbon {
    position: absolute; left: 140px; top: 798px; width: 500px; height: 60px;
  }
  .start-ribbon span {
    position: absolute; inset: 0 0 8px 0;
    display: flex; align-items: center; justify-content: center;
    font-family: "Open Sans", sans-serif; font-weight: 700;
    font-size: 22px; color: #fff; text-transform: uppercase;
  }
  .details {
    position: absolute; left: 0; right: 0; top: 872px;
    text-align: center; font-family: "Open Sans", sans-serif;
    font-weight: 700; font-size: 15px; line-height: 34px;
    text-transform: uppercase;
  }
  .contact-footer {
    position: absolute; left: 0; right: 0; bottom: 0; height: 136px;
    background: var(--footer); color: var(--footer-text);
    display: flex; flex-direction: column; align-items: center; justify-content: center;
    font-family: "Open Sans", sans-serif; font-weight: 600;
    font-size: 20px; text-transform: uppercase; line-height: 1.35;
  }
  .contact-footer .social { color: var(--link-blue); }
</style>
</head>
<body>
  <main class="poster">
    <div class="portrait" role="img" aria-label="Black silhouette of a young singer wearing headphones, singing into a vintage studio microphone"></div>

    <div class="brand">
      <div class="brand-name">MARSA <span class="brand-dot"></span></div>
      <div class="brand-sub">Student &amp; Primary Singers</div>
    </div>

    <div class="headline-band">
      <h1 class="headline">Calling Young Singers</h1>
    </div>

    <p class="invite">If you are aged 11-18, can sing and want to<br>come on tour to Germany next March-April 2016</p>

    <h2 class="needs-you">Marsa Student Singers Needs You</h2>

    <div class="start-ribbon">
      <svg width="500" height="60" viewBox="0 0 500 60" aria-hidden="true">
        <polygon points="0,14 40,14 40,56 0,56 14,35" fill="var(--red)"/>
        <polygon points="500,14 460,14 460,56 500,56 486,35" fill="var(--red)"/>
        <polygon points="40,46 56,52 56,46" fill="var(--red-dark)"/>
        <polygon points="460,46 444,52 444,46" fill="var(--red-dark)"/>
        <rect x="36" y="4" width="428" height="42" fill="var(--red)"/>
      </svg>
      <span>Starting September 2015...</span>
    </div>

    <div class="details">
      <p>Marsa Primary Singers for young singers aged 7–10 years</p>
      <p>Perform in concerts | Rehearsals twice weekly (Sun &amp; Wed)</p>
    </div>

    <footer class="contact-footer">
      <p>For more information email info@marsasingers.org</p>
      <p>See www.marsasingers.org <span class="social">Like us on Gatherly</span></p>
    </footer>
  </main>
</body>
</html>
```